Income Tax Flyer - Updates Needed

Just need to update this flyer design and give it a new look. We would like to keep all the same wording but make it stand out a little more. Our selling point is the "Same Day Tax Advance up to $6,000"

Industry/Entity Type

Lending, Small Loans, Tax Services, Title Loans, Personal Loans

```html
<!DOCTYPE html>
<html lang="en">
<head>
<meta charset="utf-8">
<title>Same Day Tax Advance Flyer</title>
<link href="https://fonts.googleapis.com/css2?family=Anton&family=Oswald:wght@300;700&family=Poppins:wght@400;600;700;800&family=Archivo:wght@800;900&display=swap" rel="stylesheet">
<style>
  :root {
    --green-deep: #06231a;
    --green-mid: #0f5a35;
    --green-brand: #0f5132;
    --red-brand: #c51f26;
    --gold-light: #fbf0a0;
    --gold-mid: #e3b838;
    --gold-dark: #b27a10;
    --white: #ffffff;
    --ink: #111111;
    --text-grey: #222222;
  }
  * { margin: 0; padding: 0; box-sizing: border-box; }
  html, body { width: 812px; height: 1200px; overflow: hidden; background: #ffffff; }
  .flyer { position: relative; width: 812px; height: 1200px; overflow: hidden; background: var(--white); font-family: "Poppins", sans-serif; }

  .hero-bg { position: absolute; inset: 0 0 auto 0; height: 800px;
    background: radial-gradient(ellipse at 48% 45%, var(--green-mid) 0%, #0a3d26 45%, var(--green-deep) 100%); }

  .money-art { position: absolute; border-radius: 50%;
    background: radial-gradient(ellipse at center, rgba(227,184,56,0.35) 0%, rgba(190,200,170,0.18) 45%, rgba(15,90,53,0) 75%); }
  .money-left { left: -40px; top: 300px; width: 300px; height: 250px; }
  .money-right-top { left: 600px; top: 230px; width: 220px; height: 140px; }
  .money-right-bottom { left: 610px; top: 480px; width: 220px; height: 150px; }
  .coins-top { left: 680px; top: -30px; width: 170px; height: 130px; }
  .coins-left-top { left: -20px; top: 40px; width: 130px; height: 100px; }

  .layer { position: absolute; left: 0; top: 0; width: 812px; height: 1200px; }

  .tag-same-day { position: absolute; left: 238px; top: 44px; width: 318px; height: 86px;
    background: var(--red-brand); transform: rotate(-2deg); display: flex; align-items: center; justify-content: center;
    box-shadow: 4px 4px 0 rgba(0,0,0,0.35); }
  .tag-same-day span { font-family: "Anton", sans-serif; font-size: 62px; color: var(--white); letter-spacing: 1px;
    text-shadow: 3px 3px 0 rgba(0,0,0,0.35); line-height: 1; }

  .headline-text { font-family: "Anton", sans-serif; }
  .headline-tax, .headline-advance, .amount-value { filter: drop-shadow(4px 4px 0 rgba(0,0,0,0.55)); }
  .amount-upto { font-family: "Oswald", sans-serif; font-weight: 300; }

  .intro-line { position: absolute; left: 0; top: 726px; width: 812px; text-align: center; font-weight: 600; font-size: 30px; line-height: 1.2; color: var(--ink); }
  .easy-advance { position: absolute; left: 0; top: 760px; width: 812px; text-align: center; font-weight: 800; font-size: 70px; line-height: 1.2; letter-spacing: -0.5px; }
  .easy-advance .word-red { color: var(--red-brand); }
  .easy-advance .word-green { color: var(--green-brand); }
  .easy-advance-reflection { top: 842px; transform: scaleY(-1); opacity: 0.16;
    -webkit-mask-image: linear-gradient(to top, #000 0%, transparent 70%); mask-image: linear-gradient(to top, #000 0%, transparent 70%); }

  .feature { position: absolute; top: 895px; width: 205px; height: 126px; border-radius: 18px; }
  .feature-green { background: var(--green-brand); }
  .feature-red { background: var(--red-brand); }
  .feature-1 { left: 64px; } .feature-2 { left: 303px; } .feature-3 { left: 543px; }
  .feature-badge { position: absolute; left: 56px; top: -46px; width: 92px; height: 92px; border-radius: 50%; border: 5px solid;
    display: flex; align-items: center; justify-content: center; }
  .badge-red { background: var(--red-brand); border-color: var(--green-brand); }
  .badge-green { background: var(--green-brand); border-color: var(--red-brand); }
  .feature-text { position: absolute; left: 0; right: 0; top: 54px; text-align: center; color: var(--white); font-weight: 700; font-size: 21px; line-height: 1.3; }

  .brand { position: absolute; left: 40px; top: 1082px; width: 228px; display: flex; align-items: center; gap: 8px; }
  .brand-mark { width: 16px; height: 16px; background: var(--red-brand); flex: none; }
  .brand-name { font-weight: 700; font-size: 19px; color: var(--green-brand); line-height: 1.2; }

  .divider { position: absolute; top: 1042px; width: 1px; height: 110px; background: #c8c8c8; }
  .divider-1 { left: 277px; } .divider-2 { left: 559px; }

  .contact-title { position: absolute; left: 292px; top: 1047px; width: 249px; height: 28px; border-radius: 5px;
    background: var(--green-brand); color: var(--white); font-weight: 700; font-size: 19px; text-align: center; line-height: 28px;
    box-shadow: 0 3px 0 #c9c9c9; letter-spacing: 0.3px; }
  .contact-row { position: absolute; left: 297px; font-size: 14px; line-height: 1; display: flex; align-items: center; gap: 6px; }
  .contact-phone { top: 1086px; font-weight: 700; color: var(--ink); }
  .contact-branch { top: 1104px; font-weight: 700; color: var(--red-brand); }
  .contact-address { position: absolute; left: 318px; top: 1120px; font-size: 14px; line-height: 19px; color: var(--text-grey); }

  .free-estimates-text { font-family: "Archivo", sans-serif; fill: var(--red-brand); }
</style>
</head>
<body>
<main class="flyer">
  <div class="hero-bg"></div>
  <div class="money-art coins-top" role="img" aria-label="Falling gold coins"></div>
  <div class="money-art coins-left-top" role="img" aria-label="Falling gold coins"></div>
  <div class="money-art money-left" role="img" aria-label="Curled hundred dollar bills and gold coins flying"></div>
  <div class="money-art money-right-top" role="img" aria-label="Curled hundred dollar bill with gold coins"></div>
  <div class="money-art money-right-bottom" role="img" aria-label="Curled hundred dollar bill with gold coins"></div>

  <svg class="layer" viewBox="0 0 812 1200" aria-hidden="true">
    <path d="M0 782 Q 470 500 812 625 L812 1200 L0 1200 Z" fill="#c51f26"/>
    <path d="M0 796 Q 470 570 812 692 L812 1200 L0 1200 Z" fill="#ffffff"/>
  </svg>

  <div class="tag-same-day"><span>SAME DAY</span></div>

  <svg class="layer headline" viewBox="0 0 812 1200">
    <defs>
      <linearGradient id="goldTax" x1="0" y1="0" x2="1" y2="0.4">
        <stop offset="0" stop-color="#b27a10"/>
        <stop offset="0.45" stop-color="#fbf0a0"/>
        <stop offset="0.7" stop-color="#e3b838"/>
        <stop offset="1" stop-color="#b27a10"/>
      </linearGradient>
      <linearGradient id="silverAdvance" x1="0" y1="0" x2="0" y2="1">
        <stop offset="0" stop-color="#ffffff"/>
        <stop offset="0.55" stop-color="#f2f2f2"/>
        <stop offset="1" stop-color="#c9ccd0"/>
      </linearGradient>
      <linearGradient id="goldAmount" x1="0" y1="0" x2="0" y2="1">
        <stop offset="0" stop-color="#fbf0a0"/>
        <stop offset="0.5" stop-color="#e3b838"/>
        <stop offset="1" stop-color="#b27a10"/>
      </linearGradient>
    </defs>
    <text class="headline-text headline-tax" x="186" y="309" font-size="212" textLength="414" lengthAdjust="spacingAndGlyphs" fill="url(#goldTax)">TAX</text>
    <text class="headline-text headline-advance" x="175" y="446" font-size="176" textLength="437" lengthAdjust="spacingAndGlyphs" fill="url(#silverAdvance)">ADVANCE</text>
    <text class="amount-upto" x="254" y="483" font-size="40" textLength="75" lengthAdjust="spacingAndGlyphs" fill="#ffffff">UPTO</text>
    <text class="headline-text amount-value" x="336" y="552" font-size="124" textLength="279" lengthAdjust="spacingAndGlyphs" fill="url(#goldAmount)">$6,000</text>
  </svg>

  <p class="intro-line">File your taxes and apply for an</p>
  <h1 class="easy-advance"><span class="word-red">EASY</span> <span class="word-green">ADVANCE!</span></h1>
  <div class="easy-advance easy-advance-reflection" aria-hidden="true"><span class="word-red">EASY</span> <span class="word-green">ADVANCE!</span></div>

  <section class="feature feature-green feature-1">
    <div class="feature-badge badge-red">
      <svg width="46" height="46" viewBox="0 0 46 46"><circle cx="23" cy="23" r="20" fill="#fff"/><text x="23" y="31" text-anchor="middle" font-family="Poppins, sans-serif" font-weight="800" font-size="24" fill="#c51f26">$</text></svg>
    </div>
    <p class="feature-text">Available In 24<br>Hours or Less</p>
  </section>
  <section class="feature feature-red feature-2">
    <div class="feature-badge badge-green">
      <svg width="46" height="46" viewBox="0 0 46 46"><circle cx="23" cy="23" r="20" fill="#fff"/><text x="23" y="31" text-anchor="middle" font-family="Poppins, sans-serif" font-weight="800" font-size="24" fill="#0f5132">$</text></svg>
    </div>
    <p class="feature-text">Choose Your<br>Loan Amount</p>
  </section>
  <section class="feature feature-green feature-3">
    <div class="feature-badge badge-red">
      <svg width="46" height="46" viewBox="0 0 46 46"><rect x="8" y="10" width="30" height="26" rx="3" fill="#fff"/><text x="23" y="30" text-anchor="middle" font-family="Poppins, sans-serif" font-weight="800" font-size="18" fill="#c51f26">$</text></svg>
    </div>
    <p class="feature-text">Quick and<br>Easy</p>
  </section>

  <div class="brand"><span class="brand-mark"></span><span class="brand-name">Keystone Lending Group</span></div>
  <div class="divider divider-1"></div>

  <div class="contact-title">CONTACT US TODAY</div>
  <div class="contact-row contact-phone">
    <svg width="14" height="14" viewBox="0 0 24 24"><circle cx="12" cy="12" r="11" fill="#0f5132"/><path d="M8 6.5c.6-.4 1.3-.3 1.6.3l1 2c.2.5.1 1-.3 1.3l-.7.6c.6 1.3 1.6 2.3 2.9 2.9l.6-.7c.3-.4.9-.5 1.3-.3l2 1c.6.3.7 1 .3 1.6l-.8 1c-.6.7-1.6.9-2.5.5-2.9-1.2-5.1-3.4-6.300-6.3-.4-.9-.2-1.9.5-2.5z" fill="#fff"/></svg>
    <span>555 0142 7788</span>
  </div>
  <div class="contact-row contact-branch">
    <svg width="14" height="16" viewBox="0 0 24 28"><path d="M12 1C7 1 3 5 3 10c0 7 9 16 9 16s9-9 9-16c0-5-4-9-9-9z" fill="none" stroke="#0f5132" stroke-width="3"/><circle cx="12" cy="10" r="3.5" fill="#0f5132"/></svg>
    <span>Riverton – North Main</span>
  </div>
  <p class="contact-address">1820-4 N. Main Street<br>Riverton, Texas 76543</p>

  <div class="divider divider-2"></div>
  <svg class="layer free-estimates" viewBox="0 0 812 1200">
    <text class="free-estimates-text" x="573" y="1114" font-size="78" font-weight="900" textLength="185" lengthAdjust="spacingAndGlyphs">FREE</text>
    <text class="free-estimates-text" x="572" y="1148" font-size="37" font-weight="800" textLength="191" lengthAdjust="spacingAndGlyphs">ESTIMATES</text>
  </svg>
</main>
</body>
</html>
```